Business Card Design

I am a video director/cameraman and photographer. I cover documentaries, corporate, government departments, educational and non profits. They could be on Tv, Vidflo or DVD to 10 or 10 thousand ppl. Some have been seen worldwide and won international awards.
I regard myself as bold and saturated...as in I want strong ideas of substance to come through in a film and that the info is valid, interesting and saturates the mind without it being geeky boring.
Need a great logo and layout for cards. My name is Barnaby Tolliver and my company is RT Media Productions.

Must have company name, my name, email, website, phone and type of films I do. I'll supply additional info for the back- which will be companies I have filmed for.

Attach image shows I like the boxes/icons idea but am open to yr ideas...Roar on!
Updates

Reason: I am charged by your designs. This is the first time I have used ths type of service and getting to know you guys is very good value for me. Please keep your creative spirit in this. I want a contemporary logo. Some have shown the way forward and a few need to show a clean, current looking image of my attitude by way of log and design. Thx to you all Barn

Industry/Entity Type

Government

```html
<!DOCTYPE html>
<html lang="en">
<head>
<meta charset="utf-8">
<title>RT Media Productions – Business Card</title>
<link rel="stylesheet" href="https://fonts.googleapis.com/css2?family=Lato:wght@400;700;900&display=swap">
<style>
  :root {
    --stage: #1f1f1f;
    --card: #2a2a2a;
    --orange: #f68e3c;
    --white: #ffffff;
    --text-light: #f2f2f2;
  }
  * { margin: 0; padding: 0; box-sizing: border-box; }
  html, body {
    width: 1200px;
    height: 1000px;
    overflow: hidden;
    background: var(--stage);
    font-family: "Lato", sans-serif;
  }
  .card {
    position: absolute;
    left: 120px;
    top: 225px;
    width: 960px;
    height: 550px;
    background: var(--card);
    overflow: hidden;
  }
  .brand {
    position: absolute;
    left: 80px;
    top: 80px;
    display: flex;
    align-items: center;
    gap: 34px;
  }
  .brand-square {
    width: 150px;
    height: 150px;
    background: var(--orange);
  }
  .brand-name {
    font-family: "Lato", sans-serif;
    font-weight: 900;
    font-size: 48px;
    line-height: 1.05;
    letter-spacing: 2px;
    text-transform: uppercase;
    color: var(--orange);
  }
  .person {
    position: absolute;
    left: 80px;
    top: 275px;
  }
  .person-name {
    font-weight: 700;
    font-size: 30px;
    color: var(--orange);
    letter-spacing: 0.5px;
  }
  .person-role {
    font-weight: 400;
    font-size: 24px;
    color: var(--text-light);
    margin-top: 2px;
    letter-spacing: 0.3px;
  }
  .contacts {
    position: absolute;
    left: 80px;
    top: 378px;
    list-style: none;
  }
  .contact {
    display: flex;
    align-items: center;
    gap: 14px;
    height: 31px;
    font-size: 23px;
    color: var(--text-light);
  }
  .contact-icon {
    width: 22px;
    height: 22px;
    flex: none;
    fill: var(--orange);
  }
  .card-band {
    position: absolute;
    left: 0;
    bottom: 0;
    width: 100%;
    height: 14px;
    display: flex;
  }
  .card-band-accent { width: 42%; background: var(--orange); }
  .card-band-light { flex: 1; background: var(--white); }
</style>
</head>
<body>
  <main class="card">
    <div class="brand">
      <div class="brand-square" aria-hidden="true"></div>
      <div class="brand-name">RT Media<br>Productions</div>
    </div>

    <div class="person">
      <p class="person-name">Barnaby Tolliver</p>
      <p class="person-role">Video Director | Cameraman | Photographer</p>
    </div>

    <ul class="contacts">
      <li class="contact">
        <svg class="contact-icon" viewBox="0 0 24 24" aria-hidden="true"><path d="M6.6 10.8a15.1 15.1 0 0 0 6.6 6.6l2.2-2.2c.3-.3.7-.4 1-.2 1.1.4 2.3.6 3.6.6.6 0 1 .4 1 1V20c0 .6-.4 1-1 1A17 17 0 0 1 3 4c0-.6.4-1 1-1h3.5c.6 0 1 .4 1 1 0 1.3.2 2.5.6 3.6.1.3 0 .7-.2 1z"/></svg>
        <span>123 456 7890</span>
      </li>
      <li class="contact">
        <svg class="contact-icon" viewBox="0 0 24 24" aria-hidden="true"><path d="M7 1h10c1.1 0 2 .9 2 2v18c0 1.1-.9 2-2 2H7c-1.1 0-2-.9-2-2V3c0-1.1.9-2 2-2zm0 3v13h10V4zm5 15a1.2 1.2 0 1 0 0 2.4 1.2 1.2 0 0 0 0-2.4z"/></svg>
        <span>123 456 7890</span>
      </li>
      <li class="contact">
        <svg class="contact-icon" viewBox="0 0 24 24" aria-hidden="true"><path d="M2 5h20v14H2zm2 2v.4l8 5.3 8-5.3V7zm0 2.8V17h16V9.8l-8 5.3z"/></svg>
        <span>barnaby@rtmediaproductions.com</span>
      </li>
      <li class="contact">
        <svg class="contact-icon" viewBox="0 0 24 24" aria-hidden="true"><path d="M12 2a10 10 0 1 0 0 20 10 10 0 0 0 0-20zm6.9 6h-2.9a15.6 15.6 0 0 0-1.4-3.6A8 8 0 0 1 18.9 8zM12 4c.8 1.2 1.5 2.5 1.9 4h-3.8c.4-1.5 1.1-2.8 1.9-4zM4.3 14a8 8 0 0 1 0-4h3.4a16.5 16.5 0 0 0 0 4zm.8 2h2.9c.3 1.3.8 2.5 1.4 3.6A8 8 0 0 1 5.1 16zM8 8H5.1a8 8 0 0 1 4.3-3.6C8.8 5.5 8.3 6.7 8 8zm4 12c-.8-1.2-1.5-2.5-1.9-4h3.8c-.4 1.5-1.1 2.8-1.9 4zm2.3-6H9.7a14.7 14.7 0 0 1 0-4h4.6a14.7 14.7 0 0 1 0 4zm.3 5.6c.6-1.1 1.1-2.3 1.4-3.6h2.9a8 8 0 0 1-4.3 3.6zm1.7-5.6a16.5 16.5 0 0 0 0-4h3.4a8 8 0 0 1 0 4z"/></svg>
        <span>www.rtmediaproductions.com</span>
      </li>
    </ul>

    <div class="card-band" aria-hidden="true">
      <div class="card-band-accent"></div>
      <div class="card-band-light"></div>
    </div>
  </main>
</body>
</html>
```